Criação de Papelaria (6 itens) para Brisa & Coral
" Serviços Exclusivos p/ Receptivo Turistico. Aluguel de Carros e Motos - Roteiros - Transfers - Reservas e Enxovais "

```html
<!DOCTYPE html>
<html lang="pt-BR">
<head>
<meta charset="UTF-8">
<title>Brisa &amp; Coral – Envelopes</title>
<link rel="stylesheet" href="https://fonts.googleapis.com/css2?family=Cinzel:wght@600&family=Montserrat:wght@400;500&display=swap">
<style>
  :root {
    --backdrop: #e9e9e7;
    --paper-white: #ffffff;
    --paper-dark: #2f2e2d;
    --paper-dark-edge: #252423;
    --gold-light: #f1c488;
    --gold: #d99a55;
    --gold-deep: #a8692f;
    --ink-gray: #6d6b68;
  }
  * { margin: 0; padding: 0; box-sizing: border-box; }
  html, body {
    width: 1200px;
    height: 1200px;
    overflow: hidden;
    background: var(--backdrop);
  }
  .stationery {
    position: relative;
    width: 1200px;
    height: 1200px;
  }
  .envelope {
    position: absolute;
    top: 260px;
    width: 470px;
    height: 680px;
    overflow: hidden;
    box-shadow: 0 18px 40px rgba(0,0,0,0.16);
  }
  .envelope--light { left: 100px; background: var(--paper-white); }
  .envelope--dark {
    left: 630px;
    background: linear-gradient(160deg, var(--paper-dark) 0%, var(--paper-dark-edge) 100%);
  }
  .envelope__flap {
    position: absolute;
    top: 0;
    left: 0;
    width: 470px;
    height: 110px;
  }
  .envelope__bottom-edge {
    position: absolute;
    left: 0;
    bottom: 0;
    width: 100%;
    height: 6px;
    background: linear-gradient(90deg, var(--gold-deep), var(--gold-light), var(--gold));
  }
  .brand-name {
    font-family: "Cinzel", serif;
    font-weight: 600;
    color: var(--gold);
    letter-spacing: 1px;
    white-space: nowrap;
  }
  .envelope--light .brand-name {
    position: absolute;
    left: 48px;
    top: 480px;
    font-size: 34px;
  }
  .contact-list {
    position: absolute;
    left: 48px;
    top: 540px;
    list-style: none;
    font-family: "Montserrat", sans-serif;
    font-size: 11px;
    line-height: 17px;
    color: var(--ink-gray);
  }
  .envelope--dark .brand-name {
    position: absolute;
    left: 0;
    width: 100%;
    top: 500px;
    text-align: center;
    font-size: 36px;
  }
  .envelope__rule {
    position: absolute;
    left: 60px;
    right: 60px;
    top: 575px;
    height: 2px;
    background: linear-gradient(90deg, var(--gold-deep), var(--gold-light), var(--gold-deep));
  }
</style>
</head>
<body>
<main class="stationery">

  <section class="envelope envelope--light" aria-label="Envelope branco">
    <svg class="envelope__flap" viewBox="0 0 470 110" aria-hidden="true">
      <defs>
        <linearGradient id="flapGoldLight" x1="0" y1="0" x2="1" y2="1">
          <stop offset="0" stop-color="var(--gold-deep)"/>
          <stop offset="0.5" stop-color="var(--gold-light)"/>
          <stop offset="1" stop-color="var(--gold)"/>
        </linearGradient>
      </defs>
      <polygon points="0,0 470,0 470,46 440,110 30,110 0,46" fill="url(#flapGoldLight)"/>
    </svg>
    <p class="brand-name">Brisa &amp; Coral</p>
    <ul class="contact-list">
      <li>Fone: (00) 3100-2200</li>
      <li>Rua das Ondas, 120 - Centro</li>
      <li>Contato: ola@brisaecoral.com</li>
      <li>Site: www.brisaecoral.com</li>
    </ul>
    <div class="envelope__bottom-edge"></div>
  </section>

  <section class="envelope envelope--dark" aria-label="Envelope escuro">
    <svg class="envelope__flap" viewBox="0 0 470 110" aria-hidden="true">
      <defs>
        <linearGradient id="flapGoldDark" x1="0" y1="0" x2="1" y2="1">
          <stop offset="0" stop-color="var(--gold-deep)"/>
          <stop offset="0.45" stop-color="var(--gold-light)"/>
          <stop offset="1" stop-color="var(--gold)"/>
        </linearGradient>
      </defs>
      <polygon points="0,0 470,0 470,46 440,110 30,110 0,46" fill="url(#flapGoldDark)"/>
    </svg>
    <p class="brand-name">Brisa &amp; Coral</p>
    <div class="envelope__rule"></div>
    <div class="envelope__bottom-edge"></div>
  </section>

</main>
</body>
</html>
```